A4 Pages

We are looking for some title pages for a children journal, we like the designs attached with use of photos and design elements particularly angles and shapes, we like drawings, icons and photos incroprated but not cartoon like.
Some photos attached to work with

Page 1)
Maple & Dove logo
incorporate the image with the MDL letters and rainbow

wording
My Learning Journal
2026
have a blank box to write the child's
have a name box

Page 2
wording
Dove Pathway Curriculum
Include the logos in the Dove Pathwey curriculum

```html
<!DOCTYPE html>
<html lang="en">
<head>
<meta charset="utf-8">
<title>Maple &amp; Dove – My Learning Journal 2026 Covers</title>
<link href="https://fonts.googleapis.com/css2?family=Fredoka:wght@600&family=Poppins:wght@400;600&family=Patrick+Hand&display=swap" rel="stylesheet">
<style>
  :root{
    --sky:#1aa7e0;
    --leaf:#8cc63f;
    --sun:#fbe816;
    --navy:#2d2a6e;
    --berry:#e8383d;
    --ocean:#28a9e0;
    --tangerine:#f47b20;
    --paper:#ffffff;
    --ink:#1c1c1c;
    --stage:#eeeeee;
    --pale-blue:#cfe9f8;
    --placeholder-soft:#e3eef5;
    --placeholder-deep:#b9d7ea;
  }
  *{margin:0;padding:0;box-sizing:border-box}
  html,body{width:871px;height:1200px;overflow:hidden;background:var(--stage)}
  .canvas{position:relative;width:871px;height:1200px}
  .page{
    position:absolute;top:317px;width:628px;height:888px;
    transform:scale(0.637);transform-origin:top left;
    background:var(--paper);overflow:hidden;
    box-shadow:0 6px 18px rgba(0,0,0,.25);
  }
  .page--front{left:20px}
  .page--back{left:451px}
  .shapes{position:absolute;inset:0;width:628px;height:888px}
  .photo{position:absolute}
  .page--front .photo{
    left:0;top:200px;width:628px;height:520px;
    background:linear-gradient(100deg,#c9a27c 0%,#e6cba8 35%,#dcc0a0 55%,#f0e2cf 80%,#e7d3bc 100%);
    -webkit-mask-image:linear-gradient(to bottom,transparent 0%,#000 25%,#000 60%,transparent 100%);
            mask-image:linear-gradient(to bottom,transparent 0%,#000 25%,#000 60%,transparent 100%);
  }
  .page--back .photo{
    left:0;top:250px;width:628px;height:480px;opacity:.35;
    background:linear-gradient(90deg,#b9b2a6 0%,#ddd6cb 40%,#8d8a84 70%,#d8d2c8 100%);
    -webkit-mask-image:linear-gradient(to bottom,transparent 0%,#000 30%,#000 60%,transparent 100%);
            mask-image:linear-gradient(to bottom,transparent 0%,#000 30%,#000 60%,transparent 100%);
  }
  .brand{position:absolute;top:42px;width:150px;text-align:center}
  .page--front .brand{left:28px}
  .page--back .brand{right:28px}
  .brand__dot{display:block;width:62px;height:62px;border-radius:50%;background:var(--sun);margin:0 auto 10px}
  .brand__name{font-family:"Fredoka",sans-serif;font-weight:600;font-size:30px;line-height:1.05;color:var(--paper)}
  .title{position:absolute;left:78px;top:548px;font-family:"Fredoka",sans-serif;font-weight:600;line-height:1}
  .title__line{display:block}
  .title__line--top{font-size:64px;color:var(--leaf)}
  .title__line--bottom{font-size:64px;color:var(--navy);margin-top:-2px}
  .title__year{font-size:88px;margin-left:10px;vertical-align:-14px;letter-spacing:1px}
  .d1{color:var(--berry)} .d2{color:var(--ocean)} .d3{color:var(--leaf)} .d4{color:var(--tangerine)}
  .name-box{
    position:absolute;left:101px;top:727px;width:426px;height:57px;
    background:var(--paper);border:1.5px solid var(--berry);border-radius:8px;
    font-family:"Poppins",sans-serif;font-size:20px;color:var(--ink);
    display:flex;align-items:center;padding:0 16px;
  }
  .name-box__line{flex:1;border-bottom:1.5px solid var(--ink);margin-left:8px;height:16px}
  .site{position:absolute;top:833px;font-family:"Poppins",sans-serif;font-weight:600;font-size:15px;color:var(--berry)}
  .page--front .site{right:40px}
  .page--back .site{left:40px}
  .pillar{position:absolute;width:124px;height:124px;margin:-62px 0 0 -62px;border-radius:50%;background:var(--paper);border:5px solid var(--ocean);padding:8px}
  .pillar__art{width:100%;height:100%;border-radius:50%;background:radial-gradient(circle at 45% 40%,var(--placeholder-soft) 0%,var(--placeholder-deep) 100%)}
  .pillar__label{position:absolute;font-family:"Patrick Hand",cursive;font-size:26px;color:var(--ink);text-align:center;width:140px;line-height:.95}
  .hub{
    position:absolute;left:311px;top:556px;width:182px;height:182px;margin:-91px 0 0 -91px;
    border-radius:50%;background:var(--paper);border:5px solid var(--ocean);
    display:flex;align-items:center;justify-content:center;text-align:center;
  }
  .hub__title{font-family:"Patrick Hand",cursive;font-weight:400;font-size:30px;line-height:1;color:var(--ink)}
</style>
</head>
<body>
<main class="canvas">

  <section class="page page--front">
    <svg class="shapes" viewBox="0 0 628 888" aria-hidden="true">
      <defs>
        <linearGradient id="fadeYellowTR" x1="1" y1="0" x2="0" y2="1">
          <stop offset="0" stop-color="#fbe816"/><stop offset="1" stop-color="#fbe816" stop-opacity="0"/>
        </linearGradient>
        <linearGradient id="fadeYellowL" x1="0" y1="0" x2="1" y2="0">
          <stop offset="0" stop-color="#fbe816" stop-opacity=".8"/><stop offset="1" stop-color="#fbe816" stop-opacity="0"/>
        </linearGradient>
        <linearGradient id="fadeBlue" x1="0" y1="0" x2="0" y2="1">
          <stop offset="0" stop-color="#cfe9f8" stop-opacity="0"/><stop offset="1" stop-color="#9fd5f3"/>
        </linearGradient>
      </defs>
      <polygon points="470,0 628,0 628,260 380,180" fill="url(#fadeYellowTR)"/>
      <polygon points="0,640 320,720 0,770" fill="url(#fadeYellowL)"/>
      <polygon points="150,640 628,640 628,820 200,820" fill="url(#fadeBlue)" opacity=".6"/>
      <polygon points="0,0 185,0 245,215 0,300" fill="var(--sky)"/>
      <polygon points="175,0 600,0 245,215" fill="var(--leaf)"/>
      <polygon points="600,0 628,0 628,10" fill="var(--sun)"/>
      <polygon points="0,785 265,775 610,888 0,888" fill="var(--leaf)"/>
      <polygon points="255,888 628,725 628,888" fill="var(--sun)"/>
      <g fill="var(--sun)">
        <circle cx="290" cy="56" r="3"/><circle cx="305" cy="56" r="3"/><circle cx="320" cy="56" r="3"/><circle cx="335" cy="56" r="3"/><circle cx="350" cy="56" r="3"/>
        <circle cx="290" cy="70" r="3"/><circle cx="305" cy="70" r="3"/><circle cx="320" cy="70" r="3"/><circle cx="335" cy="70" r="3"/><circle cx="350" cy="70" r="3"/>
        <circle cx="290" cy="84" r="3"/><circle cx="305" cy="84" r="3"/><circle cx="320" cy="84" r="3"/><circle cx="335" cy="84" r="3"/><circle cx="350" cy="84" r="3"/>
        <circle cx="105" cy="820" r="3"/><circle cx="120" cy="820" r="3"/><circle cx="135" cy="820" r="3"/><circle cx="150" cy="820" r="3"/>
        <circle cx="105" cy="834" r="3"/><circle cx="120" cy="834" r="3"/><circle cx="135" cy="834" r="3"/><circle cx="150" cy="834" r="3"/>
        <circle cx="105" cy="848" r="3"/><circle cx="120" cy="848" r="3"/><circle cx="135" cy="848" r="3"/><circle cx="150" cy="848" r="3"/>
      </g>
    </svg>
    <div class="photo" role="img" aria-label="Photo of a classroom pegboard spelling MDL in coloured pegs under a peg rainbow, wooden furniture behind"></div>
    <div class="brand"><span class="brand__dot"></span><span class="brand__name">Maple &amp; Dove</span></div>
    <h1 class="title">
      <span class="title__line title__line--top">My Learning</span>
      <span class="title__line title__line--bottom">Journal<span class="title__year"><span class="d1">2</span><span class="d2">0</span><span class="d3">2</span><span class="d4">6</span></span></span>
    </h1>
    <div class="name-box">Name:<span class="name-box__line"></span></div>
    <p class="site">mapleanddove.edu.au</p>
  </section>

  <section class="page page--back">
    <svg class="shapes" viewBox="0 0 628 888" aria-hidden="true">
      <defs>
        <linearGradient id="bFadeYellowTL" x1="0" y1="0" x2="1" y2="1">
          <stop offset="0" stop-color="#fbe816"/><stop offset="1" stop-color="#fbe816" stop-opacity="0"/>
        </linearGradient>
        <radialGradient id="bSunGlow" cx=".5" cy="1" r=".6">
          <stop offset="0" stop-color="#fbe816" stop-opacity=".8"/><stop offset="1" stop-color="#fbe816" stop-opacity="0"/>
        </radialGradient>
        <linearGradient id="bFadeBlue" x1="0" y1="0" x2="0" y2="1">
          <stop offset="0" stop-color="#cfe9f8" stop-opacity="0"/><stop offset="1" stop-color="#9fd5f3"/>
        </linearGradient>
      </defs>
      <polygon points="0,0 160,0 260,200 0,260" fill="url(#bFadeYellowTL)"/>
      <polygon points="0,650 628,650 628,830 0,830" fill="url(#bFadeBlue)" opacity=".5"/>
      <rect x="140" y="660" width="340" height="200" fill="url(#bSunGlow)"/>
      <polygon points="628,0 440,0 385,190 628,290" fill="var(--sky)"/>
      <polygon points="50,0 455,0 385,190" fill="var(--leaf)"/>
      <polygon points="0,760 360,800 200,888 0,888" fill="var(--sun)"/>
      <polygon points="280,888 628,760 628,888" fill="var(--leaf)"/>
      <g fill="var(--sun)">
        <circle cx="275" cy="56" r="3"/><circle cx="290" cy="56" r="3"/><circle cx="305" cy="56" r="3"/><circle cx="320" cy="56" r="3"/><circle cx="335" cy="56" r="3"/>
        <circle cx="275" cy="70" r="3"/><circle cx="290" cy="70" r="3"/><circle cx="305" cy="70" r="3"/><circle cx="320" cy="70" r="3"/><circle cx="335" cy="70" r="3"/>
        <circle cx="275" cy="84" r="3"/><circle cx="290" cy="84" r="3"/><circle cx="305" cy="84" r="3"/><circle cx="320" cy="84" r="3"/><circle cx="335" cy="84" r="3"/>
        <circle cx="475" cy="820" r="3"/><circle cx="490" cy="820" r="3"/><circle cx="505" cy="820" r="3"/><circle cx="520" cy="820" r="3"/>
        <circle cx="475" cy="834" r="3"/><circle cx="490" cy="834" r="3"/><circle cx="505" cy="834" r="3"/><circle cx="520" cy="834" r="3"/>
        <circle cx="475" cy="848" r="3"/><circle cx="490" cy="848" r="3"/><circle cx="505" cy="848" r="3"/><circle cx="520" cy="848" r="3"/>
      </g>
      <g stroke="var(--ocean)" stroke-width="2" fill="var(--ocean)">
        <line x1="311" y1="462" x2="311" y2="432"/><polygon points="305,436 317,436 311,426" stroke="none"/>
        <line x1="228" y1="500" x2="196" y2="475"/><polygon points="194,482 202,472 190,470" stroke="none"/>
        <line x1="394" y1="500" x2="426" y2="470"/><polygon points="420,466 428,476 432,464" stroke="none"/>
        <line x1="216" y1="556" x2="180" y2="556"/><polygon points="182,550 182,562 172,556" stroke="none"/>
        <line x1="406" y1="556" x2="442" y2="556"/><polygon points="440,550 440,562 450,556" stroke="none"/>
      </g>
    </svg>
    <div class="photo" role="img" aria-label="Faded photo of a bright classroom kitchen area"></div>
    <div class="brand"><span class="brand__dot"></span><span class="brand__name">Maple &amp; Dove</span></div>

    <div class="pillar" style="left:137px;top:366px"><div class="pillar__art" role="img" aria-label="Icon for the Inspired pillar"></div></div>
    <p class="pillar__label" style="left:67px;top:436px">Inspired</p>
    <div class="pillar" style="left:312px;top:321px"><div class="pillar__art" role="img" aria-label="Icon for the Unite pillar"></div></div>
    <p class="pillar__label" style="left:242px;top:390px">Unite</p>
    <div class="pillar" style="left:489px;top:366px"><div class="pillar__art" role="img" aria-label="Icon for the Fit pillar"></div></div>
    <p class="pillar__label" style="left:419px;top:436px">Fit</p>
    <div class="pillar" style="left:102px;top:556px"><div class="pillar__art" role="img" aria-label="Icon for the Smart Start pillar"></div></div>
    <p class="pillar__label" style="left:32px;top:626px">Smart<br>Start</p>
    <div class="pillar" style="left:524px;top:556px"><div class="pillar__art" role="img" aria-label="Icon for the Crew pillar"></div></div>
    <p class="pillar__label" style="left:454px;top:626px">Crew</p>

    <div class="hub"><h2 class="hub__title">Dove<br>Pathway<br>Curriculum</h2></div>
    <p class="site">mapleanddove.edu.au</p>
  </section>

</main>
</body>
</html>
```